Redesign of codeharborworks.net including blog.

We now have a design in layered PSD files. The design is almost there but needs some tweaking and some great coding to get it in place!

We no longer need SEO help, just brilliant coding and some design tweaks.

Please feel free to ask me any questions.

Please note:
1. This is my first time using artflockly, and as such, am not yet ready to make this a guaranteed project. I'm sure I'll be able to do that on subsequent projects when I gain more trust in the process.
2. My clients are always looking for good designers. Always. What I'm doing here is testing the process for myself. If I'm happy with your design and your work ethic, be sure that I'll be sending more work your way.

Thanks for your interest in the project.

Hello Designers! The project is now GUARANTEED!

Industry/Entity Type

Seo

Requirements
Must have
• * Same idea of having image sliders on the homepage
* Must be smartphone compatible
* High resolution images and icons supporting retina display

```html
<!DOCTYPE html>
<html lang="en">
<head>
<meta charset="utf-8">
<title>codeharborworks</title>
<link href="https://fonts.googleapis.com/css2?family=Yanone+Kaffeesatz:wght@400;700&family=Arimo:wght@400;700&display=swap" rel="stylesheet">
<style>
:root{
  --green:#5c9a1f;--green-dark:#2f5c0c;--green-light:#8fd13a;--olive:#6b8e23;
  --ink:#222;--text:#555;--muted:#888;--grey:#e8e8e8;--panel:#fff;
  --foot:#232323;--foot-line:#3a3a3a;--foot-text:#bbb;--topbar:#3a3a3a;
}
*{margin:0;padding:0;box-sizing:border-box}
html,body{width:812px;height:1200px;overflow:hidden}
body{position:relative;background:var(--grey);font-family:Arimo,Arial,sans-serif;color:var(--text)}
.abs{position:absolute}
.topbar{left:0;top:0;width:812px;height:26px;background:var(--topbar);font-size:8px;color:#fff;text-align:right;padding:8px 60px 0 0}
.topbar span{color:#aaa}
.header{left:0;top:26px;width:812px;height:82px;background:linear-gradient(#fafafa,#dcdcdc)}
.logo{left:60px;top:0;width:71px;height:75px;background:#9a9a9a;text-align:center}
.logo .mark{display:block;width:34px;height:34px;border-radius:50%;background:#fff;margin:10px auto 8px}
.logo .name{font-size:7.5px;color:#333}
.phone{left:426px;top:22px;font-size:12.5px;color:#333}
.search{left:602px;top:16px;width:151px;height:22px;border:1px solid #ccc;border-radius:11px;background:#fff;font-size:8px;color:#555;padding:6px 10px}
.search svg{position:absolute;right:8px;top:5px}
.nav{left:192px;top:56px;display:flex;font-size:9.5px;font-weight:700;color:#333}
.nav a{padding:0 14px;border-left:1px solid #888;line-height:11px;color:#333;text-decoration:none}
.nav a:first-child{border:0;padding-left:0;position:relative}
.nav a:first-child:before{content:"";position:absolute;left:0;top:-10px;width:26px;height:3px;background:var(--green)}
.hero{left:0;top:108px;width:812px;height:314px;background:radial-gradient(ellipse at 50% 40%,#6fa82e,#3d7014 70%,#2c560a);overflow:hidden}
.hero h1{position:absolute;left:58px;top:62px;font-weight:400;color:#fff;font-size:31px}
.hero p{position:absolute;left:58px;color:#fff}
.cta{left:60px;top:333px;width:143px;height:39px;border-radius:7px;background:linear-gradient(#9be04a,#4ea614);font-size:16px;font-weight:700;color:#111;padding:10px 0 0 14px}
.cta svg{position:absolute;right:10px;top:10px}
.arrow{width:28px;height:30px;background:var(--green-light)}
.hero-art{left:470px;top:20px;width:260px;height:280px;border-radius:50% 50% 40% 40%;background:radial-gradient(ellipse at 55% 35%,rgba(240,200,160,.55),rgba(200,50,50,.35) 40%,rgba(60,90,160,.25) 65%,rgba(60,112,20,0) 75%)}
.pager{left:343px;top:409px;width:107px;height:24px;background:#f4f4f4;border-radius:4px}
.pager b{position:absolute;top:8px;width:9px;height:9px;border-radius:50%;background:#999}
.svc h2{font-family:"Yanone Kaffeesatz",sans-serif;font-size:26px;font-weight:700;color:#111;top:440px}
.svc h2 em{font-style:normal;color:var(--olive)}
.card{top:480px;background:var(--panel);height:203px;font-size:7.5px;line-height:12px;text-align:center;padding:0 14px}
.card .art{width:100%;height:128px;margin:10px 0 22px}
.blog{left:0;top:700px;width:812px;height:228px;background:#fff}
.blog h2{position:absolute;left:60px;top:8px;font-family:"Yanone Kaffeesatz",sans-serif;font-size:26px;font-weight:700;color:#111}
.post{position:absolute;top:44px;width:190px}
.thumb{width:182px;height:68px}
.video{background:linear-gradient(90deg,#000 18%,#666 40%,#888 50%,#666 60%,#000 82%);position:relative}
.video i{position:absolute;left:68px;top:20px;width:44px;height:28px;background:#333;border-radius:4px}
.video i:after{content:"";position:absolute;left:17px;top:8px;border-left:11px solid #fff;border-top:6px solid transparent;border-bottom:6px solid transparent}
.date{position:absolute;left:0;width:28px;font-size:7px;line-height:12px;text-align:center;color:#333;background:#f1f1f1;padding:2px 0}
.tag{position:absolute;left:0;width:28px;height:26px;background:var(--green)}
.tag:after{content:"";position:absolute;left:8px;top:8px;width:12px;height:9px;border:2px solid #fff}
.post h3{position:absolute;left:34px;font-weight:400;font-size:12.5px;color:#222;white-space:nowrap}
.post p{position:absolute;left:34px;width:172px;font-size:7.5px;line-height:12.5px}
.more{position:absolute;left:0;width:55px;height:19px;border:1px solid #ccc;border-radius:3px;background:linear-gradient(#fff,#e6e6e6);font-size:8px;color:#333;text-align:center;line-height:17px}
.footer{left:0;top:948px;width:812px;height:252px;background:var(--foot);color:var(--foot-text)}
.col{position:absolute;top:18px;width:148px}
.col h4{font-family:"Yanone Kaffeesatz",sans-serif;font-weight:400;font-size:19px;color:#fff;padding-bottom:8px;border-bottom:1px solid var(--foot-line);margin-bottom:14px}
.col ul{list-style:none}
.col li{font-size:8px;height:22px;line-height:17px}
.res li:before{content:"›";margin-right:8px;color:#fff}
.soc li{display:flex;align-items:center;gap:10px;color:#999}
.soc li i{flex:none;width:17px;height:17px;border-radius:50%;background:#3c9ad4}
.feat .item{display:flex;gap:10px;margin-bottom:14px;font-size:7px;line-height:12px}
.feat .img{width:40px;height:40px;border:2px solid #111;flex:none}
.feat .txt{width:102px}
.feat b{font-weight:400;color:#ddd;font-size:8.5px}
.field{width:147px;height:20px;background:#1a1a1a;border:1px solid #333;margin-bottom:4px;font-size:6.5px;color:#888;padding:6px 8px}
.area{height:56px}
.submit{width:42px;height:18px;background:#1a1a1a;border:1px solid #333;font-size:7px;color:#ccc;text-align:center;line-height:16px}
.copy{left:57px;top:1150px;width:697px;height:35px;border-radius:6px;background:radial-gradient(ellipse at center,#6a9d2a,#2c4e0a);font-size:6.5px;color:#fff;text-align:center;line-height:35px}
</style>
</head>
<body>
<div class="abs topbar">Tuesday, 07 August 2012 &nbsp; <span>Contact Us &nbsp;|&nbsp; Blog</span></div>

<header class="abs header">
  <div class="abs logo"><span class="mark"></span><span class="name">codeharborworks</span></div>
  <div class="abs phone">Telephone: +1 (555) 014-2287</div>
  <div class="abs search">Search<svg width="10" height="10" viewBox="0 0 10 10"><circle cx="6" cy="4" r="3" fill="none" stroke="#2a5db0" stroke-width="1.4"/><line x1="4" y1="6" x2="1" y2="9" stroke="#2a5db0" stroke-width="1.6"/></svg></div>
  <nav class="abs nav"><a>Home</a><a>Web Development</a><a>Social Media</a><a>Server Management</a><a>Cloud Deployment</a><a>Code Review</a></nav>
</header>

<section class="abs hero">
  <h1>Is Your Code Secure?</h1>
  <p style="top:106px;font-size:23px">Do you know what a sql injection is?</p>
  <p style="top:144px;font-size:20px">If you don’t know, That’s fine.</p>
  <p style="top:184px;font-size:24px">We do! Contact Us</p>
  <div class="abs arrow" style="left:15px;top:140px"><svg width="28" height="30"><path d="M17 9l-6 6 6 6" stroke="#fff" stroke-width="3" fill="none"/></svg></div>
  <div class="abs arrow" style="left:767px;top:140px"><svg width="28" height="30"><path d="M11 9l6 6-6 6" stroke="#fff" stroke-width="3" fill="none"/></svg></div>
  <div class="abs hero-art" role="img" aria-label="Cartoon developer holding a laptop and a pencil"></div>
</section>
<div class="abs cta">Get Started<svg width="19" height="19"><circle cx="9.5" cy="9.5" r="9" fill="#fff"/><path d="M7 5l6 4.5-6 4.5z" fill="#4ea614"/></svg></div>
<div class="abs pager">
  <svg class="abs" style="left:8px;top:7px" width="8" height="10"><path d="M6 1L2 5l4 4" stroke="#333" stroke-width="1.5" fill="none"/></svg>
  <b style="left:29px"></b><b style="left:43px"></b><b style="left:57px"></b><b style="left:71px"></b>
  <svg class="abs" style="left:92px;top:7px" width="8" height="10"><path d="M2 1l4 4-4 4" stroke="#333" stroke-width="1.5" fill="none"/></svg>
</div>

<section class="svc">
  <h2 class="abs" style="left:61px">WEB <em>DEVELOPMENT</em></h2>
  <h2 class="abs" style="left:302px">SOCIAL <em>MEDIA</em></h2>
  <h2 class="abs" style="left:539px">CLOUD <em>DEPLOYMENT</em></h2>
  <div class="abs card" style="left:60px;width:228px"><div class="art" role="img" aria-label="Metal www letters with tools" style="background:radial-gradient(ellipse at 50% 45%,#b9b9b9,#e2e2e2 55%,#fff 80%)"></div>Need a web driven app, a blog, a CMS? Sure, we'll write it, set it up, deploy it, customize it until it's just the way you want it. We'll even help you with the hosting.</div>
  <div class="abs card" style="left:302px;width:224px"><div class="art" role="img" aria-label="Network of connected colourful figures" style="background:radial-gradient(ellipse at 50% 50%,#d9d6e6,#efeff3 55%,#fff 80%)"></div>Whatever your app does now, or what you would like it to do, it will probably benefit from being social.</div>
  <div class="abs card" style="left:539px;width:214px"><div class="art" role="img" aria-label="Servers and computers linked to a cloud" style="background:radial-gradient(ellipse at 50% 50%,#cfe0f0,#eef4fa 55%,#fff 80%)"></div>Want to host your site without paying for physical servers? There's a cloud for that.</div>
</section>

<section class="abs blog">
  <h2>BLOG</h2>
  <article class="post" style="left:60px">
    <div class="thumb" role="img" aria-label="Blog cover artwork" style="background:linear-gradient(90deg,#ddd,#e05a3a)"></div>
    <div class="date" style="top:76px">21 may<br>2012</div><div class="tag" style="top:104px"></div>
    <h3 style="top:76px">Lorem ipsum dolor sit amet</h3>
    <p style="top:94px">Need a web driven app, a blog, a CMS? Sure, we'll write it, set it up, deploy it, customize it until it's just the way you want it. We'll even help you with the hosting.</p>
    <div class="more" style="top:149px">Read more</div>
  </article>
  <article class="post" style="left:309px">
    <div class="thumb video" role="img" aria-label="Video still of a misty forest"><i></i></div>
    <div class="date" style="top:79px">21 may<br>2012</div><div class="tag" style="top:107px"></div>
    <h3 style="top:79px">Lorem ipsum dolor sit amet</h3>
    <p style="top:97px">Need a web driven app, a blog, a CMS? Sure, we'll write it, set it up, deploy it, customize it until it's just the way you want it. We'll even help you with the hosting.</p>
    <div class="more" style="top:152px">Read more</div>
  </article>
  <article class="post" style="left:569px">
    <div class="thumb video" role="img" aria-label="Video still of a misty forest"><i></i></div>
    <div class="date" style="top:79px">21 may<br>2012</div><div class="tag" style="top:107px"></div>
    <h3 style="top:79px">Lorem ipsum dolor sit amet</h3>
    <p style="top:97px;width:150px">Need a web driven app, a blog, a CMS? Sure, we'll write it, set it up, deploy it, customize it until it's just the way you want it.</p>
    <div class="more" style="top:152px">Read more</div>
  </article>
</section>

<footer class="abs footer">
  <div class="col res" style="left:61px"><h4>USEFUL RESOURCES</h4><ul><li>Lorem ipsum Dolor Sit Amet</li><li>Lorem ipsum Dolor Sit Amet</li><li>Lorem ipsum Dolor Sit Amet</li><li>Lorem ipsum Dolor Sit Amet</li><li>Lorem ipsum Dolor Sit Amet</li></ul></div>
  <div class="col feat" style="left:230px"><h4>FEATURED BLOG</h4>
    <div class="item"><div class="img" role="img" aria-label="Sunset photo" style="background:linear-gradient(#e9a040,#8a4a20)"></div><div class="txt"><b>Lorem Ipsum is simply</b><br>The printing and typesetting industry has been industry...</div></div>
    <div class="item"><div class="img" role="img" aria-label="Football on grass photo" style="background:linear-gradient(#7ab0e0,#3d8a22)"></div><div class="txt"><b>Lorem Ipsum is simply</b><br>The printing and typesetting industry has been industry...</div></div>
  </div>
  <div class="col soc" style="left:397px"><h4>GET SOCIAL</h4><ul><li><i></i>Follow us on Chirper</li><li><i style="background:#2f5aa8"></i>Friendship on Friendbook</li><li><i style="background:#2b7bb9"></i>Visit us on Linkwork</li><li><i style="background:#3aa8d8"></i>See our Vids on Vidora</li><li><i style="background:#e8772e"></i>Subscribe to RSS Feed</li></ul></div>
  <div class="col" style="left:564px"><h4>CONTACT US</h4><div class="field">Name</div><div class="field">Email</div><div class="field area"></div><div class="submit">Submit</div></div>
</footer>
<div class="abs copy">© COPYRIGHTS 2012. ALL RIGHTS RESERVED.</div>
</body>
</html>
```